Cover-Design im Comic Stil gesucht
Zielgruppe
eigentlich jeder der Knauser ist Kult Niveau hat und es ähnliches gut findet. Menschen zwischen 20-50 Jahren. Es soll für ein Buch sein mit dem Titel : Pfeif einfach, das reicht.
Inhalt ist: der Leser stellt eine Frage und schlägt eine beliebige Seit auf, die die Antwort enthält. (meistens scheiss drauf)
Aufgabenstellung
Es sollte ein eher Comic Stil sein, der puristisch gehalten ist. die Grösse des Buches sollte 6x6 zoll werden.

```html
<!DOCTYPE html>
<html lang="de">
<head>
<meta charset="utf-8">
<title>Pfeif einfach, das reicht – Cover</title>
<link rel="stylesheet" href="https://fonts.googleapis.com/css2?family=Anton&display=swap">
<style>
  :root {
    --page: #ffffff;
    --cover: #f8ab0e;
    --title: #5e1d0d;
    --subtitle: #6a2a12;
    --art-light: #8f4508;
    --art-dark: #5a1f0a;
  }
  html, body {
    margin: 0;
    padding: 0;
    overflow: hidden;
    background: var(--page);
  }
  .canvas {
    position: relative;
    width: 848px;
    height: 1200px;
    background: var(--page);
    overflow: hidden;
  }
  .cover {
    position: absolute;
    left: 122px;
    top: 194px;
    width: 615px;
    height: 614px;
    background: var(--cover);
    overflow: hidden;
  }
  .title {
    position: absolute;
    left: 30px;
    top: 18px;
    margin: 0;
    font-family: "Anton", "Impact", sans-serif;
    font-weight: 400;
    color: var(--title);
    text-transform: uppercase;
    white-space: nowrap;
  }
  .title-main {
    display: block;
    font-size: 138px;
    line-height: 139px;
    letter-spacing: -1px;
  }
  .title-sub {
    display: block;
    margin-top: 3px;
    font-size: 45px;
    line-height: 52px;
    color: var(--subtitle);
    letter-spacing: -0.5px;
  }
  .artwork {
    position: absolute;
    left: 223px;
    top: 321px;
    width: 349px;
    height: 240px;
    border-radius: 36px 36px 22px 22px;
    background: linear-gradient(180deg, var(--art-light) 0%, var(--art-dark) 100%);
  }
</style>
</head>
<body>
  <div class="canvas">
    <section class="cover">
      <h1 class="title">
        <span class="title-main">Pfeif<br>einfach,</span>
        <span class="title-sub">das<br>reicht.</span>
      </h1>
      <div class="artwork" role="img" aria-label="Comic-Illustration: gestreifter brauner Haufen mit langem Schatten"></div>
    </section>
  </div>
</body>
</html>
```